Criação de Layout Web-Design para Alimentos & Bebidas
A empresa queria:
" O Supermercado Vilarena está localizado em Jataí (GO), e com o intuito de divulgar suas ofertas para o publico maior de consumidores, decidiu investir no desenvolvimento de um website. "

```html
<!DOCTYPE html>
<html lang="pt-BR">
<head>
<meta charset="UTF-8">
<title>Supermercado Vilarena</title>
<link rel="stylesheet" href="https://fonts.googleapis.com/css2?family=Roboto+Condensed:wght@300;400;700&display=swap">
<style>
:root{
  --red:#c8142c;
  --navy:#2d3588;
  --green:#2f8a3c;
  --text:#3a3a3a;
  --grey:#8a8a8a;
  --line:#d4d4d4;
  --white:#ffffff;
}
*{margin:0;padding:0;box-sizing:border-box}
html,body{width:1200px;height:1200px;overflow:hidden;background:var(--white)}
body{position:relative;font-family:"Roboto Condensed",sans-serif;color:var(--text)}
.frame-lines{position:absolute;left:0;top:0;width:1200px;height:560px;z-index:2}
.brand{position:absolute;left:163px;top:50px;width:200px;height:132px;background:var(--white);
  box-shadow:0 2px 8px rgba(0,0,0,.18);display:flex;flex-direction:column;align-items:center;justify-content:center;gap:6px;z-index:3}
.brand-mark{width:34px;height:34px;border-radius:50%;background:var(--red)}
.brand-name{font-weight:700;font-size:22px;line-height:1.05;color:var(--navy);text-align:center;text-transform:uppercase}
.main-nav{position:absolute;left:382px;top:88px;display:flex;gap:30px;font-weight:700;font-size:15px;color:var(--text);z-index:3}
.contact-badge{position:absolute;left:845px;top:60px;width:192px;height:26px;background:var(--navy);color:var(--white);
  font-size:14px;font-weight:700;display:flex;align-items:center;justify-content:center;z-index:3}
.social{position:absolute;left:942px;top:94px;display:flex;gap:12px;z-index:3}
.social span{width:11px;height:11px;border-radius:50%;background:#333}
.hero{position:absolute;left:0;top:122px;width:1200px;height:410px;z-index:1;
  background:radial-gradient(ellipse at 50% 45%,#f2ede0 0%,#e4e6d4 30%,#cfdcc6 60%,#b9cab4 100%)}
.hero-copy{position:absolute;right:128px;top:218px;text-align:right;z-index:3}
.hero-title{font-weight:300;font-size:38px;line-height:1.12;color:var(--navy);text-transform:uppercase}
.hero-title b{color:var(--green);font-weight:400}
.hero-cta{display:inline-block;margin-top:14px;padding:6px 14px;background:rgba(255,255,255,.85);
  color:var(--green);font-size:15px;text-transform:uppercase}
.hero-dots{position:absolute;left:543px;top:474px;display:flex;gap:10px;z-index:3}
.hero-dots span{width:12px;height:12px;border-radius:50%;border:2px solid var(--white);background:rgba(255,255,255,.25)}
.hero-dots span:first-child{background:var(--white)}
.offers{position:absolute;left:0;top:0;width:1200px;height:1200px;z-index:4;pointer-events:none}
.offers-head{position:absolute;left:233px;top:556px;width:770px;height:40px;border-bottom:2px solid var(--line)}
.offers-tab{position:absolute;left:0;top:0;height:38px;padding:0 14px;background:var(--navy);color:var(--white);
  font-size:17px;display:flex;align-items:center;text-transform:uppercase}
.offers-tab b{font-weight:700;margin-left:5px}
.offers-tab::after{content:"";position:absolute;left:14px;bottom:-8px;border-left:8px solid transparent;border-right:8px solid transparent;border-top:8px solid var(--navy)}
.offers-note{position:absolute;right:0;top:10px;font-size:9px;color:var(--grey)}
.product{position:absolute;width:180px;text-align:center}
.product-photo{height:118px;margin:0 auto;border-radius:6px}
.product-name{margin-top:16px;font-size:17px;color:var(--text)}
.product-price{font-size:18px;font-weight:700;color:var(--green)}
.photo-sponge{width:150px;background:linear-gradient(160deg,#f4e11a,#e8c40f 60%,#d42a2a)}
.photo-can{width:72px;background:linear-gradient(180deg,#e9ecf4,#2b4fa3 45%,#d8243a)}
.photo-biscuit{width:130px;background:linear-gradient(90deg,#c32a25,#f0e6dc 50%,#8a4a2a)}
.photo-wafer{width:150px;height:80px;margin:20px auto 18px;background:linear-gradient(160deg,#f1d34a,#7a3b1c)}
.more-offers{position:absolute;left:220px;top:1074px;width:783px;border-bottom:3px solid #666;text-align:center;
  font-size:17px;color:#555;padding-bottom:4px;text-transform:uppercase}
.more-arrow{position:absolute;left:602px;top:1106px;border-left:10px solid transparent;border-right:10px solid transparent;border-top:10px solid #555}
</style>
</head>
<body>
<div class="hero" role="img" aria-label="Foto de uma cliente sorridente segurando sacolas com pães e verduras em um corredor de supermercado"></div>

<svg class="frame-lines" viewBox="0 0 1200 560" aria-hidden="true">
  <path d="M0 55 Q600 48 1200 55" fill="none" stroke="var(--red)" stroke-width="5"/>
  <path d="M0 60 Q600 56 1200 60" fill="none" stroke="#bfbfbf" stroke-width="2"/>
  <path d="M0 122 L1200 122" fill="none" stroke="#cfcfcf" stroke-width="1"/>
  <path d="M0 500 Q600 555 1200 500 L1200 560 L0 560 Z" fill="var(--white)"/>
  <path d="M0 500 Q600 555 1200 500" fill="none" stroke="var(--red)" stroke-width="5"/>
  <path d="M0 508 Q600 562 1200 508" fill="none" stroke="#bfbfbf" stroke-width="2"/>
</svg>

<header>
  <div class="brand">
    <span class="brand-mark"></span>
    <span class="brand-name">Supermercado<br>Vilarena</span>
  </div>
  <nav class="main-nav">
    <span>HOME</span><span>INSTITUCIONAL</span><span>OFERTAS</span><span>RECEITAS</span><span>CONTATO</span>
  </nav>
  <div class="contact-badge">ATENDIMENTO: (64) 3631-2048</div>
  <div class="social"><span></span><span></span><span></span><span></span></div>
</header>

<div class="hero-copy">
  <h1 class="hero-title">Aqui sua <b>satisfação</b><br>é garantida</h1>
  <span class="hero-cta">Confira nossas promoções</span>
</div>
<div class="hero-dots"><span></span><span></span><span></span><span></span><span></span></div>

<section class="offers">
  <div class="offers-head">
    <div class="offers-tab">Produtos em <b>oferta</b></div>
    <div class="offers-note">*Ofertas válidas até 30/11 ou enquanto durarem os estoques</div>
  </div>

  <div class="product" style="left:215px;top:620px"><div class="product-photo photo-sponge" role="img" aria-label="Embalagem de palha de aço"></div><p class="product-name">Nome do Produto</p><p class="product-price">R$ 1,05</p></div>
  <div class="product" style="left:419px;top:620px"><div class="product-photo photo-can" role="img" aria-label="Lata de creme de leite"></div><p class="product-name">Nome do Produto</p><p class="product-price">R$ 1,05</p></div>
  <div class="product" style="left:623px;top:620px"><div class="product-photo photo-biscuit" role="img" aria-label="Pacotes de biscoitos"></div><p class="product-name">Nome do Produto</p><p class="product-price">R$ 1,05</p></div>
  <div class="product" style="left:834px;top:620px"><div class="product-photo photo-wafer" role="img" aria-label="Barra de chocolate"></div><p class="product-name">Nome do Produto</p><p class="product-price">R$ 1,05</p></div>

  <div class="product" style="left:215px;top:870px"><div class="product-photo photo-sponge" role="img" aria-label="Embalagem de palha de aço"></div><p class="product-name">Nome do Produto</p><p class="product-price">R$ 1,05</p></div>
  <div class="product" style="left:419px;top:870px"><div class="product-photo photo-can" role="img" aria-label="Lata de creme de leite"></div><p class="product-name">Nome do Produto</p><p class="product-price">R$ 1,05</p></div>
  <div class="product" style="left:623px;top:870px"><div class="product-photo photo-biscuit" role="img" aria-label="Pacotes de biscoitos"></div><p class="product-name">Nome do Produto</p><p class="product-price">R$ 1,05</p></div>
  <div class="product" style="left:834px;top:870px"><div class="product-photo photo-wafer" role="img" aria-label="Barra de chocolate"></div><p class="product-name">Nome do Produto</p><p class="product-price">R$ 1,05</p></div>

  <div class="more-offers">Mais ofertas</div>
  <div class="more-arrow"></div>
</section>
</body>
</html>
```